Real Estate Investment Company Needs A Business Card Designed

I need a business card designed for my use. We are a real estate investment company based in Omaha, Nebraska that specializes in buying, rehabbing and selling single family and multifamily properties. Would love designs that incorporate our logo and colors

Industry/Entity Type

Business

Contact Information for Business Card

Marlow Pettigrew | President & CEO
4837 North 52nd Avenue, Ste 200
Omaha, NE 68214
(402) 555-7428
marlow@quillfenhomes.example
www.QuillfenHomes.example

Font styles to use
Serif

Colors
0255a3
3276b5

Requirements
Must have
• Our logo

```html
<!DOCTYPE html>
<html lang="en">
<head>
<meta charset="utf-8">
<title>Quillfen Homes – Business Card</title>
<link rel="stylesheet" href="https://fonts.googleapis.com/css2?family=Montserrat:wght@600;700&family=Roboto+Condensed:wght@400&display=swap">
<style>
  :root {
    --brand-blue: #0255a3;
    --brand-blue-light: #3276b5;
    --blue-deep: #0a66b0;
    --blue-top: #3a8ccc;
    --silver: #a9adb2;
    --silver-light: #d6d8db;
    --ink: #333b44;
    --card-white: #f6f6f6;
    --backdrop: #b9b9b9;
  }
  * { margin: 0; padding: 0; box-sizing: border-box; }
  html, body { width: 1200px; height: 576px; overflow: hidden; }
  body { background: var(--backdrop); position: relative; font-family: "Roboto Condensed", sans-serif; }

  .card {
    position: absolute;
    top: 140px;
    width: 484px;
    height: 294px;
    border-radius: 14px;
    overflow: hidden;
  }

  /* Front */
  .card-front {
    left: 82px;
    background: linear-gradient(180deg, var(--blue-top) 0%, var(--blue-deep) 45%, var(--brand-blue) 100%);
  }
  .front-mark {
    position: absolute;
    left: 50%;
    top: 62px;
    width: 104px;
    height: 104px;
    margin-left: -52px;
    border-radius: 50%;
    background: #ffffff;
  }
  .front-name {
    position: absolute;
    left: 0; right: 0;
    top: 190px;
    text-align: center;
    font-family: "Montserrat", sans-serif;
    font-weight: 700;
    font-size: 27px;
    letter-spacing: 0.5px;
    color: #ffffff;
  }

  /* Back */
  .card-back {
    left: 602px;
    background: var(--card-white);
  }
  .back-mark {
    position: absolute;
    left: 54px;
    top: 36px;
    width: 84px;
    height: 84px;
    border-radius: 50%;
    background: var(--brand-blue-light);
  }
  .back-name {
    position: absolute;
    left: 18px;
    width: 160px;
    top: 134px;
    text-align: center;
    font-family: "Montserrat", sans-serif;
    font-weight: 700;
    font-size: 16px;
    color: var(--brand-blue);
  }
  .person {
    position: absolute;
    left: 246px;
    top: 46px;
  }
  .person-name {
    font-family: "Montserrat", sans-serif;
    font-weight: 700;
    font-size: 20px;
    color: var(--brand-blue);
  }
  .person-name .surname { color: var(--brand-blue-light); }
  .person-title {
    margin-top: 4px;
    font-size: 13px;
    color: var(--ink);
  }
  .contact {
    position: absolute;
    left: 246px;
    top: 160px;
    list-style: none;
    font-size: 13.5px;
    color: var(--ink);
  }
  .contact li { display: flex; align-items: center; height: 18px; }
  .contact svg { width: 11px; height: 11px; margin-right: 10px; fill: var(--brand-blue); }
  .contact .accent { color: var(--brand-blue-light); }
  .address {
    position: absolute;
    left: 246px;
    top: 221px;
    font-size: 13.5px;
    line-height: 18px;
    color: var(--ink);
    font-style: normal;
  }
  .footer-band {
    position: absolute;
    left: 0; bottom: 0;
    width: 100%;
    height: 14px;
  }
</style>
</head>
<body>

  <section class="card card-front" aria-label="Card front">
    <div class="front-mark"></div>
    <div class="front-name">QUILLFEN HOMES</div>
  </section>

  <section class="card card-back" aria-label="Card back">
    <div class="back-mark"></div>
    <div class="back-name">QUILLFEN HOMES</div>

    <div class="person">
      <div class="person-name">Marlow <span class="surname">Pettigrew</span></div>
      <div class="person-title">President &amp; CEO</div>
    </div>

    <ul class="contact">
      <li>
        <svg viewBox="0 0 12 12" aria-hidden="true"><path d="M1 3.5C1 2 2.5 1 6 1s5 1 5 2.5V5H8.5V3.8h-5V5H1z"/><path d="M2.5 6h7l1.2 5H1.3z"/></svg>
        (402) 555-7428
      </li>
      <li>
        <svg viewBox="0 0 12 12" aria-hidden="true"><path d="M0.5 2h11v8h-11z M1.5 3l4.5 3.5L10.5 3" fill="none" stroke="#0255a3" stroke-width="1.2"/></svg>
        marlow@quillfenhomes.example
      </li>
      <li>
        <svg viewBox="0 0 12 12" aria-hidden="true"><g fill="none" stroke="#0255a3" stroke-width="1"><circle cx="6" cy="6" r="5"/><ellipse cx="6" cy="6" rx="2.2" ry="5"/><path d="M1 6h10"/></g></svg>
        www.<span class="accent">QuillfenHomes</span>.example
      </li>
    </ul>

    <address class="address">
      4837 North 52nd Avenue, Ste 200<br>
      Omaha, NE 68214
    </address>

    <svg class="footer-band" viewBox="0 0 484 14" preserveAspectRatio="none" aria-hidden="true">
      <defs>
        <linearGradient id="band-blue" x1="0" x2="1" y1="0" y2="0">
          <stop offset="0" stop-color="#0255a3"/>
          <stop offset="1" stop-color="#3276b5"/>
        </linearGradient>
        <linearGradient id="band-silver" x1="0" x2="1" y1="0" y2="0">
          <stop offset="0" stop-color="#d6d8db"/>
          <stop offset="1" stop-color="#a9adb2"/>
        </linearGradient>
      </defs>
      <rect x="0" y="0" width="484" height="14" fill="url(#band-silver)"/>
      <polygon points="0,2 338,2 322,14 0,14" fill="url(#band-blue)"/>
    </svg>
  </section>

</body>
</html>
```